6x9 Postcard "401k Rollover" to market Individuals to transfer their retirement savings to our firm

Formats: .jpg, .png, .psd, .ai
Dimensions: See uploaded documents

We need a postcard to encourage people 45-65 years olds to transfer their retirement plan assets to our financial advising firm. We have uploaded an example we've been working please feel free to use your artistic license to make it look good images etc. You do not need to copy it word for word, we welcome creativity.

Suggested Wording:

We make it easy to rollover your old 401k

Spread the word! If you or someone you know has a 401k with a former employer or has reached age 59 1/2, consider a 401k rollover

The Marlowe Financial team can help rollover your old 401k

Advantages of a rollover: control over your accounts, more investment options, professional investment management, consolidate and simplify your accounts, guaranteed lifetime income options, help from a team of dedicated advisors

Make the most of your old 401k with a new Rollover IRA, speak with a trusted advisor today, (661)555-0142

If the QWM logo is used it MUST be used with the name "Gerald Pruitt" near it to clearly associate the two. if the words are used they Must be after his name and in all caps like this "Gerald Pruitt, ACCREDITED WEALTH STEWARD TM" [super script TM]. These are rules of the QWM trade mark.

Target Market(s)

Age 45 to 65 with sizable assets in 401k retirement plans

Industry/Entity Type

Investment Advisory

Font styles to use
Serif
Sans Serif
Decorative
Script

Colors

Designer to choose colors to be used in the design.

Requirements
Must have
• The post card MUST contain the following text at least 8pt font:
• Securities offered through Ember Ridge Securities, L.P. Member - NEVOC/TALQ | 4875 North Elm Rd, Ste 120, Lancaster, CA 93536 | 800.555.0173 | CA Ins. Lic. #0K48391, #0713948, #0K52806, #0619427
• Must have website and phone number:
• www.geraldpruittadvisory.example
• (661) 555-0142
Nice to have
• We would like the design to convey: Trust, Safety, Growth, Wealth, Planning, Strength, Stable, Peace of Mind, Time, Classic, Legacy

```html
<!DOCTYPE html>
<html lang="en">
<head>
<meta charset="utf-8">
<title>401K Rollover Postcard</title>
<link rel="stylesheet" href="https://fonts.googleapis.com/css2?family=Roboto+Condensed:wght@400;500;700&family=Roboto:wght@700&display=swap">
<style>
  :root {
    --page-bg: #e0e0e0;
    --teal: #1e6a77;
    --navy: #1c3a66;
    --gold: #f5c518;
    --arc: #f2b705;
    --green: #1f6b2a;
    --green-box: #1a6b1f;
    --ink: #222222;
    --mark-dark: #1e1e1e;
    --white: #ffffff;
  }
  * { margin: 0; padding: 0; box-sizing: border-box; }
  html, body { width: 800px; height: 1200px; overflow: hidden; }
  body {
    position: relative;
    background: var(--page-bg);
    font-family: "Roboto Condensed", "Arial Narrow", sans-serif;
    color: var(--ink);
  }
  .abs { position: absolute; }

  /* Front */
  .front { left: 23px; top: 86px; width: 753px; height: 500px; background: var(--white); overflow: hidden; }
  .front-header {
    left: 0; top: 0; width: 753px; height: 88px; background: var(--teal);
    color: var(--white); font-size: 26px; line-height: 37px; padding: 6px 0 0 22px;
  }
  .front-photo {
    left: 330px; top: 88px; width: 423px; height: 412px;
    background: linear-gradient(160deg, #f3f1ec 0%, #dcd6cc 35%, #b9a58c 60%, #8a6d52 80%, #5d5e63 100%);
  }
  .front-curve { left: 0; top: 0; }
  .brand { display: flex; align-items: center; gap: 8px; }
  .brand-square { width: 18px; height: 18px; background: var(--gold); }
  .brand-name { font-weight: 700; color: var(--ink); }
  .front .brand { left: 20px; top: 110px; }
  .front .brand-name { font-size: 40px; line-height: 1; }
  .front .brand-square { width: 28px; height: 28px; }
  .planner-line { left: 19px; top: 173px; font-size: 14.5px; font-weight: 500; }
  .planner-line sup, .back-planner sup { font-size: 0.6em; }
  .lead-question { left: 18px; top: 202px; font-size: 22px; color: #2b2b2b; }
  .offer-box {
    left: 18px; top: 236px; width: 349px; height: 102px; background: var(--navy);
    color: var(--gold); text-align: center; box-shadow: 0 3px 4px rgba(0,0,0,0.35);
  }
  .offer-title { font-size: 35px; line-height: 40px; padding-top: 2px; font-weight: 500; }
  .offer-text { font-size: 20px; line-height: 29px; }
  .call-label { left: 38px; top: 343px; font-size: 19px; color: var(--green); }
  .call-number { left: 36px; top: 360px; font-size: 49px; color: var(--green); font-weight: 500; }
  .front-web { left: 31px; top: 414px; font-size: 27px; color: var(--navy); font-weight: 500; }
  .plan-note { left: 120px; top: 445px; font-family: "Roboto", Arial, sans-serif; font-size: 10px; font-weight: 700; }
  .disclosure { left: 22px; top: 463px; font-size: 11px; line-height: 15px; font-weight: 500; }

  .label { width: 800px; text-align: center; font-size: 24px; font-weight: 500; color: #111; }
  .label-front { top: 590px; }
  .label-back { top: 1154px; }

  /* Back */
  .back { left: 28px; top: 654px; width: 742px; height: 496px; overflow: hidden; }
  .back-photo {
    left: 0; top: 0; width: 742px; height: 496px;
    background: linear-gradient(120deg, #f4f3ef 0%, #ebe8e2 40%, #e7e8ea 70%, #dcdee0 100%);
  }
  .address-area { left: 382px; top: 184px; width: 360px; height: 232px; background: var(--white); }
  .address-band { left: 41px; top: 416px; width: 701px; height: 80px; background: var(--white); }
  .stamp { left: 646px; top: 12px; width: 75px; height: 87px; border: 2px solid #111; background: var(--white); }
  .back .brand { left: 402px; top: 16px; gap: 10px; }
  .back .brand-name { font-size: 34px; line-height: 1; color: var(--mark-dark); }
  .back .brand-square { width: 22px; height: 22px; background: var(--mark-dark); }
  .back-planner { left: 402px; top: 56px; font-size: 8px; font-weight: 500; white-space: nowrap; }
  .back-headline {
    left: 15px; top: 20px; width: 375px; font-size: 23px; line-height: 31px;
    color: var(--green); white-space: nowrap;
  }
  .advantages-title { left: 4px; top: 88px; width: 294px; padding-left: 22px; font-size: 20px; color: var(--navy); border-bottom: 2px solid var(--navy); line-height: 26px; }
  .advantages { left: 46px; top: 117px; list-style: none; color: var(--green); font-size: 19px; }
  .advantages li { display: flex; align-items: center; gap: 4px; height: 26.5px; }
  .advantages svg { flex: none; }
  .cta-box {
    left: 20px; top: 287px; width: 329px; height: 110px; background: var(--green-box);
    color: var(--white); text-align: center;
  }
  .cta-text { font-size: 16px; line-height: 23px; padding-top: 11px; }
  .cta-phone { font-size: 29px; line-height: 40px; font-weight: 500; margin-top: 4px; }
</style>
</head>
<body>

<section class="abs front">
  <div class="abs front-header">If you or someone you know has a 401K with a former employer<br>“or” has reached Age 59 1/2*, Consider a 401K ROLLOVER...</div>
  <div class="abs front-photo" role="img" aria-label="Photo of a smiling senior couple shaking hands with an advisor across a table"></div>
  <svg class="abs front-curve" width="753" height="500" viewBox="0 0 753 500" aria-hidden="true">
    <path d="M0 88 L341 88 C328 250 400 420 525 500 L0 500 Z" fill="#ffffff"/>
    <path d="M341 88 C328 250 400 420 525 500" fill="none" stroke="var(--arc)" stroke-width="5"/>
  </svg>
  <div class="abs brand"><span class="brand-square"></span><span class="brand-name">QWM</span></div>
  <div class="abs planner-line">Gerald Pruitt, ACCREDITED WEALTH STEWARD<sup>TM</sup></div>
  <div class="abs lead-question">Looking for Inverstment Options?</div>
  <div class="abs offer-box">
    <div class="offer-title">Come to Us !</div>
    <div class="offer-text">Our Firm excels at providing<br>excellent service on a personal level !!</div>
  </div>
  <div class="abs call-label">Call Us</div>
  <div class="abs call-number">(661) 555-0142</div>
  <div class="abs front-web">www.geraldpruittadvisory.example</div>
  <div class="abs plan-note">*subject to employer plan rules</div>
  <div class="abs disclosure">Securities offered through Ember Ridge Securities, L.P. Member - NEVOC/TALQ<br>4875 North Elm Rd, Ste 120, Lancaster, CA 93536 | 800.555.0173 | CA Ins.</div>
</section>
<div class="abs label label-front">Front</div>

<section class="abs back">
  <div class="abs back-photo" role="img" aria-label="Faded photo of a senior couple meeting with an advisor"></div>
  <div class="abs address-area"></div>
  <div class="abs address-band"></div>
  <div class="abs stamp"></div>
  <div class="abs brand"><span class="brand-square"></span><span class="brand-name">QWM</span></div>
  <div class="abs back-planner">Gerald Pruitt, ACCREDITED WEALTH STEWARD<sup>TM</sup></div>
  <div class="abs back-headline">The Gerald Pruitt Financial Team can<br>help rollover your old 401K</div>
  <div class="abs advantages-title">Advantages of a rollover</div>
  <ul class="abs advantages">
    <li><svg width="18" height="16" viewBox="0 0 18 16"><rect x="1" y="4" width="11" height="11" fill="none" stroke="#1c3a66" stroke-width="1.6"/><path d="M3 9 L6.5 12.5 L16 2" fill="none" stroke="#1c3a66" stroke-width="2"/></svg>Control over your accounts</li>
    <li><svg width="18" height="16" viewBox="0 0 18 16"><rect x="1" y="4" width="11" height="11" fill="none" stroke="#1c3a66" stroke-width="1.6"/><path d="M3 9 L6.5 12.5 L16 2" fill="none" stroke="#1c3a66" stroke-width="2"/></svg>More investment options</li>
    <li><svg width="18" height="16" viewBox="0 0 18 16"><rect x="1" y="4" width="11" height="11" fill="none" stroke="#1c3a66" stroke-width="1.6"/><path d="M3 9 L6.5 12.5 L16 2" fill="none" stroke="#1c3a66" stroke-width="2"/></svg>Professional investment management</li>
    <li><svg width="18" height="16" viewBox="0 0 18 16"><rect x="1" y="4" width="11" height="11" fill="none" stroke="#1c3a66" stroke-width="1.6"/><path d="M3 9 L6.5 12.5 L16 2" fill="none" stroke="#1c3a66" stroke-width="2"/></svg>Consolidate abd simplify</li>
    <li><svg width="18" height="16" viewBox="0 0 18 16"><rect x="1" y="4" width="11" height="11" fill="none" stroke="#1c3a66" stroke-width="1.6"/><path d="M3 9 L6.5 12.5 L16 2" fill="none" stroke="#1c3a66" stroke-width="2"/></svg>Guaranteed lifetime income options</li>
    <li><svg width="18" height="16" viewBox="0 0 18 16"><rect x="1" y="4" width="11" height="11" fill="none" stroke="#1c3a66" stroke-width="1.6"/><path d="M3 9 L6.5 12.5 L16 2" fill="none" stroke="#1c3a66" stroke-width="2"/></svg>Help from a team of dedicated advisors</li>
  </ul>
  <div class="abs cta-box">
    <div class="cta-text">Make the most of your 401k with a<br>new rollover IRA, speak with a trusted advisor,</div>
    <div class="cta-phone">CALL 661-555-0142</div>
  </div>
</section>
<div class="abs label label-back">Back</div>

</body>
</html>
```